Packaging Design for Prime Sea Lipid 2400 MG

Project Overview:
Design a premium packaging box for Prime Sea Lipid 2400 MG capsules. The design should convey a balance between pharmaceutical credibility and luxury branding. The product is part of Velbrook Nutrition’s high-end supplement line, and its visual identity should reflect both scientific integrity and elite status.

Product Details:
Name: Prime Sea Lipid 2400 MG

Box Dimensions: 83mm (W) x 41mm (D) x 112mm (H)

Brand: Velbrook Nutrition

Key Ingredient: Omega-3 Fish Oil (High EPA & DHA)

Design Goals:
Simplicity & Sophistication:
A clean, minimal layout that avoids visual clutter while maintaining a high-end feel.

Pharmaceutical Aesthetic:
Should resemble a medical-grade product with a modern, science-driven aesthetic. Think clean lines, sharp typefaces, cool-toned color palettes (white, silver, dark gray, hints of cool blue).

Luxury Elements:
Incorporate luxury design cues—premium finishes like soft-touch matte or subtle foil stamping (e.g., silver or orange foiling). Avoid looking like a typical supplement; this is more of a boutique wellness product.

Branding:
Must prominently feature the Velbrook Nutrition orange icon logo (attached) on the front or top panel—this is the main brand signature and should remain unaltered.

Target Audience:
Health-conscious professionals and affluent consumers aged 30–60 who prioritize premium wellness products and trust clinically-backed formulations.

Mandatory Elements:
Product Name: Prime Sea Lipid 2400 MG

Velbrook Nutrition orange icon logo (attached)

Dimensions adhered to strictly

Space for supplement facts (on back or side panel)

UPC/Barcode placeholder (bottom or side)

FDA disclaimer (small text, back panel)

Tone & Style References:
Quorn packaging (clean, clinical, elegant)

Tillet or Du Colvane (luxury meets minimalism)

Modern pharmaceutical branding (bioscience style fonts, Swiss layout influence)

Deliverables:
Box dieline design (print-ready, with bleed/crop marks)

3D mockup of the box (front + side view)

Editable source file (AI/PSD)

pharmaceutical / supplements retail

FFF300
FFF600
FEFA6F
FFFEC7
FFFEE8

• Velbrook Nutrition logo

```html
<!DOCTYPE html>
<html lang="en">
<head>
<meta charset="utf-8">
<title>Prime Sea Lipid 2400 MG – Packaging Panels</title>
<link href="https://fonts.googleapis.com/css2?family=Poppins:wght@400;500;600;700&family=Roboto+Condensed:wght@400;500&display=swap" rel="stylesheet">
<style>
  :root {
    --bg: #f4f4f4;
    --ink: #2b2c2e;
    --ink-soft: #4a4b4e;
    --band-dark: #2a2b2d;
    --orange: #e0701f;
    --silver: #a9aaac;
    --light-text: #e6e6e6;
    --white: #ffffff;
  }
  * { margin: 0; padding: 0; box-sizing: border-box; }
  html, body { width: 1200px; height: 1200px; overflow: hidden; background: var(--bg); }
  body { position: relative; font-family: "Poppins", sans-serif; color: var(--ink); }

  .dieline { position: absolute; left: 150px; top: 128px; display: flex; box-shadow: 0 10px 30px rgba(0,0,0,0.08); }

  /* Side panel */
  .side-panel {
    position: relative; width: 300px; height: 945px;
    background: linear-gradient(180deg, #f2f2f2, #e4e4e4);
    border-right: 1px solid #d4d4d4; overflow: hidden;
  }
  .side-panel .brand { position: absolute; left: 34px; top: 100px; display: flex; align-items: center; gap: 8px; }
  .side-panel .brand-dot { width: 14px; height: 14px; border-radius: 50%; background: var(--orange); }
  .side-panel .brand-name { font-size: 14px; font-weight: 500; color: var(--ink-soft); }
  .side-title { position: absolute; left: 34px; top: 160px; font-family: "Roboto Condensed", sans-serif; font-weight: 500; font-size: 25px; color: var(--ink); }
  .side-copy {
    position: absolute; left: 34px; top: 235px; width: 240px;
    font-family: "Roboto Condensed", sans-serif; font-size: 12.5px; line-height: 1.75; color: var(--ink-soft);
  }
  .side-copy h3 { font-weight: 400; font-size: 12.5px; color: var(--orange); margin-top: 18px; }
  .side-copy h3:first-child { margin-top: 0; }
  .side-copy .indent { padding-left: 8px; }
  .side-copy .gap { margin-top: 18px; }
  .side-band { position: absolute; left: 0; bottom: 0; width: 100%; height: 155px; background: var(--band-dark); }
  .side-band::before { content: ""; position: absolute; left: 0; top: -10px; width: 100%; height: 10px; background: var(--silver); }
  .made-in { position: absolute; left: 0; right: 0; top: 850px; text-align: center; font-family: "Roboto Condensed", sans-serif; font-size: 11px; color: #c9c9c9; }

  /* Front panel */
  .front-panel { position: relative; width: 600px; height: 945px; overflow: hidden; }
  .front-art { position: absolute; inset: 0; }
  .front-art svg { width: 100%; height: 100%; display: block; }

  .front-panel .brand { position: absolute; left: 61px; top: 128px; display: flex; align-items: center; gap: 12px; }
  .front-panel .brand-dot { width: 30px; height: 30px; border-radius: 50%; background: var(--orange); }
  .front-panel .brand-name { font-size: 24px; font-weight: 500; color: var(--ink-soft); }

  .product-name {
    position: absolute; left: 60px; top: 212px;
    font-size: 84px; font-weight: 700; line-height: 104px; letter-spacing: 0.5px; color: var(--ink);
  }
  .potency { position: absolute; left: 62px; top: 418px; font-size: 68px; font-weight: 700; line-height: 1; color: var(--orange); }
  .tagline { position: absolute; left: 62px; top: 508px; width: 400px; font-size: 27px; font-weight: 600; line-height: 1.3; color: var(--ink); }
  .rule { position: absolute; left: 62px; top: 598px; width: 385px; height: 2px; background: var(--ink); }
  .supplement-pill {
    position: absolute; left: 62px; top: 622px;
    padding: 1px 16px; border: 1.5px solid var(--ink-soft); border-radius: 30px;
    font-size: 25px; line-height: 1.45; color: var(--ink-soft);
  }
  .epa-dha { position: absolute; left: 86px; top: 686px; font-size: 18px; color: var(--ink-soft); }
  .count-badge {
    position: absolute; left: 62px; top: 736px; height: 50px;
    display: flex; align-items: center; gap: 10px;
    padding: 0 18px; border-radius: 8px; background: var(--orange);
    color: var(--white); font-size: 22px; font-weight: 600;
  }
  .count-badge svg { width: 20px; height: 20px; }

  .benefit { position: absolute; left: 64px; top: 822px; display: flex; align-items: center; gap: 12px; }
  .benefit-icon { width: 50px; height: 50px; border-radius: 50%; border: 3px dashed #cfcfcf; }
  .benefit-divider { width: 2px; height: 50px; background: #cfcfcf; }
  .benefit-text { font-size: 18px; font-weight: 500; line-height: 1.3; color: var(--light-text); }
  .source-note { position: absolute; right: 22px; top: 812px; text-align: right; font-size: 17px; line-height: 1.35; color: var(--light-text); }
</style>
</head>
<body>
  <main class="dieline">
    <section class="side-panel" aria-label="Side panel">
      <div class="brand"><span class="brand-dot"></span><span class="brand-name">Velbrook Nutrition</span></div>
      <h2 class="side-title">PRIME SEA LIPID</h2>
      <div class="side-copy">
        <h3>Suggested Use:</h3>
        <p>Take one softgel daily with food.</p>
        <h3>Key Ingredients:</h3>
        <p>Omega-3 Fatty Acids: 2400mg</p>
        <p class="indent">- EPA (Eicosapentaenoic Acid): [25]mg</p>
        <p class="indent">- DHA (Docosahexaenoic Acid): [35]mg</p>
        <p class="gap">May help support a healthy heart and brain function.</p>
        <p class="gap">[Brand Promise/Value]: Committed to Premium Quality &amp; Purity]</p>
      </div>
      <div class="side-band"></div>
      <div class="made-in">MADE IN THE US</div>
    </section>

    <section class="front-panel" aria-label="Front panel">
      <div class="front-art">
        <svg viewBox="0 0 600 945" preserveAspectRatio="none">
          <defs>
            <linearGradient id="lightFace" x1="0" y1="0" x2="0" y2="1">
              <stop offset="0" stop-color="#efefef"/>
              <stop offset="1" stop-color="#e2e2e2"/>
            </linearGradient>
            <linearGradient id="sweepFace" x1="0" y1="0" x2="0" y2="1">
              <stop offset="0" stop-color="#d6d6d7"/>
              <stop offset="0.5" stop-color="#8b8c8f"/>
              <stop offset="1" stop-color="#2c2d2f"/>
            </linearGradient>
            <linearGradient id="helixTone" x1="0" y1="0" x2="1" y2="1">
              <stop offset="0" stop-color="#dcdcdc" stop-opacity="0"/>
              <stop offset="0.5" stop-color="#d0d0d1" stop-opacity="0.7"/>
              <stop offset="1" stop-color="#dcdcdc" stop-opacity="0"/>
            </linearGradient>
          </defs>
          <rect width="600" height="945" fill="url(#lightFace)"/>
          <rect x="330" y="200" width="210" height="460" fill="url(#helixTone)" role="img" aria-label="Faint DNA helix illustration"/>
          <rect x="0" y="775" width="600" height="15" fill="var(--silver)"/>
          <rect x="0" y="790" width="600" height="155" fill="#2a2b2d"/>
          <path d="M600 283 C560 450 520 600 470 720 C430 820 400 880 370 945 L600 945 Z" fill="url(#sweepFace)"/>
          <path d="M600 283 C572 430 540 580 495 700 C460 800 430 870 405 945" fill="none" stroke="#f3f3f3" stroke-width="5" opacity="0.75"/>
          <rect x="480" y="520" width="120" height="260" fill="#5a5b5e" opacity="0.18" role="img" aria-label="Subtle hexagon molecule pattern"/>
        </svg>
      </div>

      <div class="brand"><span class="brand-dot"></span><span class="brand-name">Velbrook Nutrition</span></div>
      <h1 class="product-name">PRIME SEA<br>LIPID</h1>
      <div class="potency">2400 MG</div>
      <p class="tagline">High Potency Omega-3 Formula.</p>
      <div class="rule"></div>
      <div class="supplement-pill">Dietary Supplement</div>
      <div class="epa-dha">With High EPA &amp; DHA</div>
      <div class="count-badge">
        <svg viewBox="0 0 24 24"><path d="M12 1 L14.5 9.5 L23 12 L14.5 14.5 L12 23 L9.5 14.5 L1 12 L9.5 9.5 Z" fill="#ffffff"/></svg>
        60 Softgels
      </div>

      <div class="benefit">
        <span class="benefit-icon"></span>
        <span class="benefit-divider"></span>
        <span class="benefit-text">Suppot Brain<br>Function</span>
      </div>
      <p class="source-note">Sourced from Pure<br>Fish Oils.</p>
    </section>
  </main>
</body>
</html>
```